Letters From a Quiet Harbor - Book Cover

I need a cover for my book, front and back.

The book is formatted as, 8 x 10.

Originally, a friend drew a crude rough draft that I really liked, but it never got finished. If you want to work off of it, you can check it out here. The page also contains plenty of information about the book itself.

http://www.backerbay.example/projects/tealoaf/letters-from-a-quiet-harbor

You will be paid whether or not the backerbay meets its goal. I will be making a hardcover copy in the future so I may look for a 2nd version of the cover if I really like more than one.

If you want to make an original cover, I like the concept of a lighthouse in the middle of a dark gloomy city, but you're welcome to design whatever you are inspired to draw.

Thanks for helping me get this project one step closer to being ready to share.
Updates

Thank you to everyone who submitted. As the deadline approaches, I will narrow down the selections to 3 choices. That will give everyone else some time to make a last minute change or submit another concept. You all did a great job following what I wanted and giving me a lot to contemplate.

Thank you to all the designers who participated. You all came up with some great stuff and it was difficult to choose. I will be using this site for more contests in the future. I'll be sure to invite you all back when I do.

Target Market(s)

Hoping to get people ages 25-40 to buy my book as a gift for people ages 18-25.

Industry/Entity Type

Work

Requirements
Nice to have
• Some inclusion of a lighthouse, even if it's not the main item of focus. Include the word "obsanity" hidden somewhere within the design.

```html
<!DOCTYPE html>
<html lang="en">
<head>
<meta charset="utf-8">
<title>Letters From a Quiet Harbor – Cover Spread</title>
<link rel="stylesheet" href="https://fonts.googleapis.com/css2?family=Ubuntu:wght@400&family=Kaushan+Script&display=swap">
<style>
  :root {
    --night: #0b0303;
    --ember-dark: #3a0c06;
    --ember: #a8300f;
    --flame: #d9661a;
    --glow: #f2a24a;
    --ground: #050202;
    --cream: #f6e7c9;
    --script-orange: #f08a2a;
    --ink: #1a0d06;
  }
  * { margin: 0; padding: 0; box-sizing: border-box; }
  html, body {
    width: 1200px; height: 706px; overflow: hidden; background: var(--night);
  }
  .cover-spread {
    position: relative; width: 1200px; height: 706px; overflow: hidden;
    font-family: "Ubuntu", "Trebuchet MS", sans-serif;
  }
  .harbor-scene {
    position: absolute; inset: 0;
    background:
      radial-gradient(ellipse 420px 60px at 620px 320px, rgba(255,214,160,0.55), transparent 70%),
      radial-gradient(ellipse 700px 260px at 380px 380px, rgba(242,162,74,0.85), transparent 70%),
      radial-gradient(ellipse 500px 220px at 980px 400px, rgba(217,102,26,0.7), transparent 70%),
      linear-gradient(180deg, var(--night) 0%, var(--ember-dark) 14%, var(--ember) 30%, var(--flame) 52%, var(--glow) 64%, var(--flame) 70%);
  }
  .harbor-scene::after {
    content: ""; position: absolute; inset: 0;
    background: radial-gradient(ellipse 560px 340px at 1200px 0px, rgba(11,3,3,0.9) 0%, rgba(11,3,3,0.6) 50%, transparent 100%);
  }
  .ground {
    position: absolute; left: 0; right: 0; top: 493px; bottom: 0;
    background: var(--ground);
  }
  .back-cover { position: absolute; left: 0; top: 0; width: 570px; height: 706px; }
  .back-title {
    position: absolute; left: 92px; width: 380px; top: 205px; text-align: center;
  }
  .title-lead {
    color: var(--cream); letter-spacing: 2px; text-transform: uppercase; font-weight: 400;
  }
  .title-script {
    font-family: "Kaushan Script", cursive; color: var(--script-orange);
  }
  .back-title .title-lead { font-size: 18px; line-height: 22px; }
  .back-title .title-script { font-size: 28px; line-height: 34px; }
  .blurb {
    position: absolute; left: 92px; top: 267px; width: 382px;
    font-size: 11.5px; line-height: 14.6px; letter-spacing: 1px;
    text-align: justify; color: var(--ink);
  }
  .spine {
    position: absolute; left: 568px; top: 0; width: 60px; height: 706px;
  }
  .spine-author {
    position: absolute; top: 14px; left: 0; right: 0; text-align: center;
    font-size: 12px; line-height: 15px; letter-spacing: 1px; color: var(--cream);
  }
  .spine-title {
    position: absolute; left: 44px; top: 338px;
    transform-origin: 0 0; transform: rotate(90deg);
    white-space: nowrap; display: flex; align-items: baseline; gap: 16px;
  }
  .spine-title .title-lead { font-size: 16px; letter-spacing: 1.5px; }
  .spine-title .title-script { font-size: 25px; }
  .front-cover { position: absolute; left: 628px; top: 0; right: 0; height: 706px; }
  .front-title {
    position: absolute; left: 116px; width: 320px; top: 76px; text-align: center;
  }
  .front-title .title-lead { font-size: 27px; line-height: 34px; letter-spacing: 2.5px; }
  .front-title .title-script { font-size: 46px; line-height: 56px; }
  .front-author {
    position: absolute; left: 116px; width: 320px; top: 660px; text-align: center;
    font-size: 18px; letter-spacing: 2px; color: var(--cream);
  }
</style>
</head>
<body>
<main class="cover-spread">
  <div class="harbor-scene" role="img" aria-label="Painted dusk sky in burnt orange and red, a lighthouse on the right sending a pale beam across the sky, dark silhouetted rooftops along the shore"></div>
  <div class="ground"></div>

  <section class="back-cover">
    <div class="back-title">
      <p class="title-lead">Letters From a</p>
      <p class="title-script">Quiet Harbor</p>
    </div>
    <p class="blurb">Lorem ipsum dolor sit amet, consectetur adipisicing elit, sed do eiusmod tempor incididunt ut labore et dolore magna aliqua. Ut enim ad minim veniam, quis nostrud exercitation ullamco laboris nisi ut aliquip ex ea commodo consequat. Duis aute irure dolor in reprehenderit in voluptate velit esse cillum dolore eu fugiat nulla pariatur. Excepteur sint occaecat cupidatat non proident, sunt in culpa qui officia deserunt mollit anim id est laborum.</p>
  </section>

  <section class="spine">
    <p class="spine-author">Evan<br>Hollis</p>
    <div class="spine-title">
      <span class="title-lead">Letters From a</span>
      <span class="title-script">Quiet Harbor</span>
    </div>
  </section>

  <section class="front-cover">
    <div class="front-title">
      <h1 class="title-lead">Letters From a</h1>
      <p class="title-script">Quiet Harbor</p>
    </div>
    <p class="front-author">Evan Hollis</p>
  </section>
</main>
</body>
</html>
```